Banner Designs for Drone Defense Ad Campaign

Harborlyte is a security consulting and services company that offers a service called SkyMarrowin. SkyMarrowin helps our customers identify security risks from drones and develops comprehensive protection programs. We are looking for a designer to create a banner ad in three sizes for our campaign.
Target Market(s)
Our campaign is geared to the sports and entertainment industry, specifically large event venues and their security operation.
Industry/Entity Type
Security
Font styles to use
Other font styles liked:
- Raleway
Requirements
Must have
- Banner Objective
The visual and textual content of the banner should prompt the viewer to quickly identify the service offered and the information that is available to download.
Banner Design
Logo: SkyMarrowin logo
Call to Action Button in Red: Get It Here (On Right or or Upper Right)
Title in Larger Font: Guide to UAS Risk Mitigation
Subtitle in smaller Font: 5 Steps to Develop Your Comprehensive UAS Defense Program
Background: Stadium with a drone flying in foreground
Font: Raleway
Banner Sizes
1 - 1200x670 pixels
2 - 1510x196 pixels
3 - 1200x628 pixels

```html
<!DOCTYPE html>
<html lang="en">
<head>
<meta charset="utf-8">
<title>Guide to UAS Risk Mitigation – SkyMarrowin by Harborlyte</title>
<link rel="stylesheet" href="https://fonts.googleapis.com/css2?family=Raleway:wght@400;500;700;800;900&display=swap">
<style>
  :root {
    --ink-black: #000000;
    --white: #ffffff;
    --cta-red: #d0251f;
    --sky-teal: #2e9aa8;
    --sky-amber: #b07a45;
    --sky-mid: #4f7380;
    --roof-dark: #1b2630;
    --crowd-dark: #1a232c;
    --crowd-mid: #2c3a46;
    --crowd-red: #8a3a3e;
    --veil-blue: rgba(30, 90, 160, 0.5);
    --veil-light: rgba(140, 185, 220, 0.22);
  }
  * { margin: 0; padding: 0; box-sizing: border-box; }
  html, body {
    width: 1200px;
    height: 670px;
    overflow: hidden;
    background: var(--ink-black);
  }
  .banner {
    position: relative;
    width: 1200px;
    height: 670px;
    font-family: "Raleway", sans-serif;
    color: var(--white);
    overflow: hidden;
  }
  .hero-scene {
    position: absolute;
    left: 0; top: 0;
    width: 1200px;
    height: 560px;
    background:
      /* drone in the foreground: bright white body with dark surround */
      radial-gradient(ellipse 55px 40px at 905px 285px, rgba(245, 245, 245, 0.95), rgba(200, 205, 210, 0.6) 55%, transparent 100%),
      radial-gradient(ellipse 40px 30px at 858px 370px, rgba(230, 230, 230, 0.75), transparent 100%),
      radial-gradient(ellipse 260px 170px at 900px 280px, rgba(8, 10, 14, 0.75), transparent 75%),
      /* big screen glow on the right stand */
      radial-gradient(ellipse 70px 45px at 1110px 235px, rgba(150, 175, 190, 0.6), transparent 100%),
      /* warm red glow over the lower crowd */
      radial-gradient(ellipse 520px 220px at 430px 520px, rgba(170, 60, 60, 0.7), transparent 80%),
      /* crowd stands */
      linear-gradient(180deg, transparent 0, transparent 175px, var(--crowd-mid) 185px, var(--crowd-dark) 300px, #202a33 420px, #161d24 560px),
      /* stadium roof band */
      linear-gradient(180deg, transparent 0, transparent 95px, rgba(120, 140, 150, 0.55) 100px, var(--roof-dark) 130px, var(--roof-dark) 180px, transparent 181px),
      /* dusk sky */
      linear-gradient(90deg, var(--sky-amber) 0%, var(--sky-mid) 45%, var(--sky-teal) 100%);
  }
  .hero-veil {
    position: absolute;
    left: 0; top: 0;
    width: 1200px;
    height: 560px;
  }
  .headline {
    position: absolute;
    left: 48px;
    top: 186px;
  }
  .headline-title {
    font-weight: 900;
    font-size: 70px;
    line-height: 56px;
    letter-spacing: 0.5px;
    text-transform: uppercase;
    padding-top: 6px;
  }
  .headline-subtitle {
    margin-top: 10px;
    font-weight: 400;
    font-size: 22px;
    line-height: 35px;
    letter-spacing: 0.3px;
    text-transform: uppercase;
  }
  .footer-bar {
    position: absolute;
    left: 0; top: 560px;
    width: 1200px;
    height: 110px;
    background: var(--ink-black);
  }
  .brand {
    position: absolute;
    left: 50px;
    top: 38px;
    width: 160px;
  }
  .brand-name {
    font-weight: 700;
    font-size: 22px;
    line-height: 24px;
  }
  .brand-parent {
    font-weight: 700;
    font-size: 11px;
    line-height: 14px;
    margin-top: 4px;
    padding-left: 70px;
  }
  .cta-button {
    position: absolute;
    left: 985px;
    top: 32px;
    width: 165px;
    height: 47px;
    background: var(--cta-red);
    color: var(--white);
    font-weight: 700;
    font-size: 20px;
    letter-spacing: -0.5px;
    display: flex;
    align-items: center;
    justify-content: center;
    text-decoration: none;
  }
</style>
</head>
<body>
  <div class="banner">
    <div class="hero-scene" role="img" aria-label="Packed stadium at dusk under an amber-to-teal sky, with a white camera drone hovering in the right foreground"></div>

    <svg class="hero-veil" viewBox="0 0 1200 560" aria-hidden="true">
      <polygon points="0,125 310,0 780,0 640,175 135,560 0,560" fill="var(--veil-blue)"/>
      <polygon points="230,0 780,0 640,175" fill="var(--veil-light)"/>
    </svg>

    <div class="headline">
      <h1 class="headline-title">Guide to UAS<br>Risk Mitigation</h1>
      <p class="headline-subtitle">5 Steps to Develop Your Comprehensive<br>UAS Defense Program</p>
    </div>

    <div class="footer-bar">
      <div class="brand">
        <div class="brand-name">SkyMarrowin</div>
        <div class="brand-parent">By Harborlyte</div>
      </div>
      <a class="cta-button" href="#">GET IT HERE</a>
    </div>
  </div>
</body>
</html>
```